LEARN Business Skills so you can Earn a good living

size of the poster is 8”x 10.75" plus 0.25" bleed.
Please leave 1 inch on the bottoum for footer
I want a design a poster that will attract people's attention.
I appreciate a creative ad however the ad should not take away from being able to clearly read the text.
-I also appreciate a simple creative ad that is not too busy.
-you can use graphics, vectors, or pictures of real people.
-however, if you use real people it should be a white male that is wearing a white shirt and look like a professional person.

Target Market(s)

Potential young business people

Industry/Entity Type

education

Requirements
Must have
• easy to read the text
Nice to have
• I would like a "creative" simple ad that is easy to be read
Should not have
• pictures of women

```html
<!DOCTYPE html>
<html lang="en">
<head>
<meta charset="utf-8">
<title>Business Enrichment Course Poster</title>
<link rel="stylesheet" href="https://fonts.googleapis.com/css2?family=Playfair+Display:ital,wght@0,600;0,800;0,900;1,400&family=DM+Sans:ital,wght@0,400;0,500;1,400&family=Sacramento&display=swap">
<style>
  :root {
    --stage: #6e6e6e;
    --paper: #eeeeef;
    --paper-shade: #e2e3e6;
    --navy: #27397a;
    --blue: #2f5aa3;
    --orange: #e68a2e;
    --ink: #2a3466;
    --muted-line: #9a9ca6;
  }
  * { box-sizing: border-box; margin: 0; padding: 0; }
  html, body { width: 1200px; height: 1200px; overflow: hidden; }
  body { background: var(--stage); position: relative; font-family: "DM Sans", sans-serif; }

  .poster {
    position: absolute; left: 190px; top: 22px; width: 820px; height: 1156px;
    background: linear-gradient(180deg, var(--paper) 0%, #f1f1f2 55%, var(--paper-shade) 100%);
    overflow: hidden;
  }
  .city-backdrop {
    position: absolute; left: 0; top: 200px; width: 820px; height: 520px;
    background: linear-gradient(180deg, rgba(200,202,208,0) 0%, rgba(196,198,204,0.55) 45%, rgba(210,212,216,0.35) 80%, rgba(230,231,233,0) 100%);
  }
  .brand-tab {
    position: absolute; left: 322px; top: 0; width: 175px; height: 210px;
  }
  .brand-tab svg { position: absolute; inset: 0; }
  .brand-name {
    position: absolute; left: 0; right: 0; top: 62px;
    text-align: center; color: #fff;
    font-family: "DM Sans", sans-serif; font-weight: 500;
    font-size: 30px; line-height: 1.05; letter-spacing: 0.5px;
  }
  .growth-illustration {
    position: absolute; left: 552px; top: 206px; width: 178px; height: 160px;
    background: linear-gradient(135deg, rgba(47,90,163,0.15) 0%, rgba(47,90,163,0.75) 100%);
    border-radius: 6px;
  }
  .headline {
    position: absolute; left: 82px; top: 270px;
    font-family: "Playfair Display", serif; font-weight: 900;
    color: var(--blue); line-height: 0.98; letter-spacing: -1px;
  }
  .headline .line-one { display: block; font-size: 96px; }
  .headline .line-two { display: block; font-size: 92px; color: var(--navy); letter-spacing: -2px; }
  .headline-script {
    position: absolute; left: 250px; top: 430px;
    font-family: "Sacramento", cursive; color: var(--orange);
    font-size: 150px; line-height: 1;
  }
  .tagline {
    position: absolute; left: 0; right: 0; top: 540px; text-align: center;
    font-style: italic; font-size: 23px; color: var(--ink);
  }
  .skills-heading {
    position: absolute; left: 0; right: 0; top: 612px; text-align: center;
    font-family: "Playfair Display", serif; font-weight: 600;
    font-size: 27px; color: var(--ink);
  }
  .skills-heading strong { font-weight: 800; }
  .benefit {
    position: absolute; top: 668px; width: 200px; text-align: center;
  }
  .benefit-icon {
    width: 112px; height: 112px; margin: 0 auto;
    background: linear-gradient(135deg, var(--navy) 0%, var(--blue) 100%);
    border-radius: 22px 22px 0 22px;
  }
  .benefit-label {
    margin-top: 24px; font-size: 22px; line-height: 1.22; color: var(--ink); font-weight: 500;
  }
  .divider {
    position: absolute; top: 662px; width: 1px; height: 190px; background: var(--muted-line);
  }
  .topic-list {
    position: absolute; left: 60px; right: 60px; top: 885px;
    text-align: center; font-size: 14px; line-height: 26.5px; color: var(--ink);
  }
  .topic-list .sep { color: var(--orange); margin: 0 3px; }
</style>
</head>
<body>
<main class="poster">
  <div class="city-backdrop" role="img" aria-label="Faded photograph of a city skyline with a tall skyscraper"></div>

  <div class="brand-tab">
    <svg width="175" height="210" viewBox="0 0 175 210">
      <polygon points="0,0 175,0 175,210 0,210" fill="var(--blue)"/>
      <polygon points="0,190 175,210 0,210" fill="var(--orange)"/>
    </svg>
    <div class="brand-name">SkillRise<br>Academy</div>
  </div>

  <div class="growth-illustration" role="img" aria-label="Illustration of a businessman with a laptop riding a rising blue growth arrow beside a briefcase"></div>

  <h1 class="headline">
    <span class="line-one">BUSINESS</span>
    <span class="line-two">ENRICHMENT</span>
  </h1>
  <div class="headline-script">Course</div>

  <p class="tagline">A proven success of helping people in their livelihoods</p>

  <h2 class="skills-heading"><strong>Business skills</strong> that will help you:</h2>

  <div class="benefit" style="left:54px">
    <div class="benefit-icon">
      <svg width="112" height="112" viewBox="0 0 112 112" fill="none" stroke="#fff" stroke-width="3">
        <circle cx="54" cy="58" r="34"/>
        <circle cx="46" cy="52" r="9"/>
        <path d="M30 78c2-10 9-15 16-15s14 5 16 15"/>
        <path d="M68 70v12M75 64v18M82 70v10"/>
        <polygon points="76,24 80,33 89,34 82,40 84,49 76,44 68,49 70,40 63,34 72,33" fill="var(--orange)" stroke="none"/>
      </svg>
    </div>
    <div class="benefit-label">Get a<br>Quality Job</div>
  </div>
  <div class="divider" style="left:277px"></div>

  <div class="benefit" style="left:291px">
    <div class="benefit-icon">
      <svg width="112" height="112" viewBox="0 0 112 112" fill="none" stroke="#fff" stroke-width="3">
        <circle cx="38" cy="40" r="11" fill="var(--orange)" stroke="none"/>
        <path d="M32 44l5-5 4 3 6-6M43 36h4v4" stroke="#fff" stroke-width="2"/>
        <path d="M24 72h64l-4 14H28z"/>
        <path d="M24 80h64"/>
        <path d="M70 72V30M70 44c-6-2-10-8-10-14 6 0 10 6 10 14zM70 44c6-2 10-8 10-14-6 0-10 6-10 14zM70 58c-6-2-10-8-10-12 6 0 10 4 10 12zM70 58c6-2 10-8 10-12-6 0-10 4-10 12z"/>
        <path d="M40 72c0-6 4-10 10-10M40 72c-2-5-6-8-10-8"/>
      </svg>
    </div>
    <div class="benefit-label">Start/Grow<br>Your Business</div>
  </div>
  <div class="divider" style="left:543px"></div>

  <div class="benefit" style="left:541px">
    <div class="benefit-icon">
      <svg width="112" height="112" viewBox="0 0 112 112" fill="none" stroke="#fff" stroke-width="3">
        <path d="M26 88l22-24 10 10 26-30M74 40h12v12"/>
        <path d="M26 88h58V58"/>
        <path d="M32 24l2 6 6 2-6 2-2 6-2-6-6-2 6-2z M48 22l1.5 4 4 1.5-4 1.5-1.5 4-1.5-4-4-1.5 4-1.5z M36 40l2 5 5 2-5 2-2 5-2-5-5-2 5-2z" fill="var(--orange)" stroke="none"/>
      </svg>
    </div>
    <div class="benefit-label">Increase Your<br>Salary</div>
  </div>

  <p class="topic-list">
    Business Administration<span class="sep">|</span>Small Business Management<span class="sep">|</span>Finance<span class="sep">|</span>Investments<span class="sep">|</span>Computers<span class="sep">|</span><br>
    Accounting<span class="sep">|</span>Sales Marketing<span class="sep">|</span>Project Management Interviewing Skills<span class="sep">|</span>Business Law<span class="sep">|</span><br>
    Negotiation<span class="sep">|</span>Public Speaking<span class="sep">|</span>Import/Export<span class="sep">|</span>Information Technoloy<span class="sep">|</span>Distribution<span class="sep">|</span><br>
    Marketing<span class="sep">|</span>Ledgerly<span class="sep">|</span>Real Estate<span class="sep">|</span>Health Care<span class="sep">|</span>Management<span class="sep">|</span>Shopvale
  </p>
</main>
</body>
</html>
```